Weightloss company needs Business Card

We want a business card that is clean and professional, yet portrays that we are a friendly, innovative, and versatile program designed to fit the needs of our clients.
I would like there to be 2 sides, one side having an appointment card, and the other side containing the logo and business information. There can be decorations on both sides. The logo is attached.

Target Market(s)

Men and women 40-60

Industry/Entity Type

Business

Contact Information for Business Card

Font styles to use
Sans Serif

Requirements
Must have
• The logo, space for business information
Nice to have
• The colors in the logo
Should not have
• No pictures of people or food

```html
<!DOCTYPE html>
<html lang="en">
<head>
<meta charset="utf-8">
<title>Renewal Turn — Business Card</title>
<link href="https://fonts.googleapis.com/css2?family=Poppins:wght@400;600&display=swap" rel="stylesheet">
<style>
  :root {
    --bg: #2b2b2d;
    --card: #ffffff;
    --red: #e8203a;
    --cyan: #3fb6e6;
    --ink: #1c1c1c;
    --white: #ffffff;
  }
  html, body {
    margin: 0;
    padding: 0;
    width: 1200px;
    height: 900px;
    overflow: hidden;
    background: var(--bg);
    font-family: "Poppins", sans-serif;
  }
  .canvas {
    position: relative;
    width: 1200px;
    height: 900px;
  }
  .card {
    position: absolute;
    width: 700px;
    height: 400px;
    background: var(--card);
    border-radius: 26px;
    overflow: hidden;
    box-shadow: 0 14px 30px rgba(0,0,0,0.45);
  }
  .card--appointment { left: 110px; top: 40px; }
  .card--contact { left: 390px; top: 460px; }

  .brand {
    position: absolute;
    display: flex;
    align-items: center;
    gap: 10px;
    font-weight: 600;
    font-size: 30px;
    color: var(--red);
    letter-spacing: 0.5px;
  }
  .brand__dot {
    width: 18px;
    height: 18px;
    border-radius: 50%;
    background: var(--cyan);
  }
  .card--appointment .brand { left: 60px; top: 110px; }
  .card--contact .brand { left: 60px; top: 90px; }

  .appointment__label {
    position: absolute;
    left: 90px;
    top: 205px;
    font-size: 16px;
    color: var(--cyan);
    letter-spacing: 0.5px;
  }
  .appointment__field {
    position: absolute;
    display: flex;
    align-items: flex-end;
    gap: 10px;
    font-size: 18px;
    color: var(--ink);
  }
  .appointment__field span.rule {
    display: block;
    height: 1px;
    background: var(--ink);
    margin-bottom: 6px;
  }
  .field--name { left: 90px; top: 238px; }
  .field--name .rule { width: 480px; }
  .field--date { left: 120px; top: 283px; }
  .field--date .rule { width: 470px; }
  .field--time { left: 150px; top: 328px; }
  .field--time .rule { width: 460px; }

  .band {
    position: absolute;
    left: 0;
    top: 190px;
    width: 100%;
    height: 162px;
    background: var(--red);
  }
  .person {
    position: absolute;
    left: 40px;
    top: 208px;
    width: 290px;
    text-align: right;
    color: var(--white);
  }
  .person__name {
    font-size: 28px;
    font-weight: 600;
    color: var(--cyan);
    line-height: 1.05;
    margin: 0;
  }
  .person__role {
    font-size: 15px;
    margin: 0 0 14px;
    letter-spacing: 0.5px;
  }
  .person__address {
    font-size: 17px;
    line-height: 1.35;
    margin: 0;
  }
  .contacts {
    position: absolute;
    left: 360px;
    top: 214px;
    list-style: none;
    margin: 0;
    padding: 0;
    color: var(--white);
    font-size: 17px;
  }
  .contacts li {
    display: flex;
    align-items: center;
    gap: 10px;
    line-height: 1.6;
  }
  .contacts svg { width: 14px; height: 14px; flex: none; }
</style>
</head>
<body>
<main class="canvas">

  <section class="card card--appointment" aria-label="Appointment side">
    <div class="brand"><span class="brand__dot"></span>Renewal Turn</div>
    <div class="appointment__label">APPOINTMENT</div>
    <div class="appointment__field field--name">Name:<span class="rule"></span></div>
    <div class="appointment__field field--date">Date:<span class="rule"></span></div>
    <div class="appointment__field field--time">Time:<span class="rule"></span></div>
  </section>

  <section class="card card--contact" aria-label="Contact side">
    <div class="brand"><span class="brand__dot"></span>Renewal Turn</div>
    <div class="band"></div>
    <div class="person">
      <p class="person__name">MARCUS ELLERY</p>
      <p class="person__role">DIRECTOR</p>
      <p class="person__address">Palm Avenue, 40512<br>Harbor City, Coastland</p>
    </div>
    <ul class="contacts">
      <li>
        <svg viewBox="0 0 24 24" fill="none" stroke="#fff" stroke-width="2.2" stroke-linecap="round" stroke-linejoin="round"><path d="M5 3h4l2 5-3 2a12 12 0 0 0 6 6l2-3 5 2v4a2 2 0 0 1-2 2A17 17 0 0 1 3 5a2 2 0 0 1 2-2z"/></svg>
        +330 5182-7743
      </li>
      <li>
        <svg viewBox="0 0 24 24" fill="none" stroke="#fff" stroke-width="2.2" stroke-linejoin="round"><rect x="2" y="5" width="20" height="14" rx="1"/><path d="M2 6l10 7 10-7"/></svg>
        info@renewalturn.com
      </li>
      <li>
        <svg viewBox="0 0 24 24" fill="none" stroke="#fff" stroke-width="2.2"><circle cx="12" cy="12" r="10"/><path d="M2 12h20M12 2c3 3 3 17 0 20M12 2c-3 3-3 17 0 20"/></svg>
        www.renewalturn.com
      </li>
    </ul>
  </section>

</main>
</body>
</html>
```